I need to rebrand my public user portal for a new/modern look and feel

I want to take my current user web portal and redesign the look of it. I have included 2 samples of my current user portal and would like options to create a new functional look. This main page below will modify based on the tabs on the top left. Any questions please ask.

```html
<!DOCTYPE html>
<html lang="en">
<head>
<meta charset="utf-8">
<title>Dashboard</title>
<link href="https://fonts.googleapis.com/css2?family=Poppins:wght@400;500;600;700&display=swap" rel="stylesheet">
<style>
:root{
  --blue-dark:#0b4a82;
  --blue-mid:#1366a6;
  --blue-light:#1a8bc8;
  --head:#0e4f8e;
  --red:#9c3437;
  --panel:#f8f9fb;
  --card:#eef1f6;
  --ink:#16181d;
  --muted:#8a8f98;
  --link:#1565a7;
  --chip:#eceef2;
}
*{box-sizing:border-box;margin:0;padding:0}
html,body{width:1200px;height:771px;overflow:hidden}
body{font-family:"Poppins",sans-serif;color:var(--ink);
  background:linear-gradient(120deg,var(--blue-dark) 0%,var(--blue-mid) 55%,var(--blue-light) 100%);position:relative}
.sidebar{position:absolute;left:0;top:0;width:222px;height:771px;color:#fff}
.brand{position:absolute;left:30px;top:30px;font-size:16px;font-weight:700;line-height:1.1;letter-spacing:.5px;display:flex;align-items:center;gap:8px}
.brand .mark{width:26px;height:26px;border-radius:50%;background:#fff}
.btn-report{position:absolute;left:17px;top:100px;width:190px;height:45px;border-radius:23px;background:var(--red);color:#fff;display:flex;align-items:center;justify-content:center;gap:8px;font-size:13.5px;font-weight:600}
.nav{position:absolute;left:18px;top:171px;width:189px;list-style:none}
.nav li{height:38px;margin-bottom:4.5px;border-radius:8px;display:flex;align-items:center;gap:12px;padding-left:13px;font-size:13px;font-weight:600}
.nav li.active{background:rgba(6,40,80,.45)}
.nav svg{width:16px;height:16px;fill:#fff}
.logout{position:absolute;left:31px;top:672px;display:flex;align-items:center;gap:12px;font-size:13px;font-weight:600}
.copy{position:absolute;left:18px;top:719px;font-size:10.5px;line-height:15px;color:rgba(255,255,255,.5)}
.main{position:absolute;left:222px;top:17px;width:960px;height:737px;background:var(--panel);border-radius:16px}
.title{position:absolute;left:27px;top:22px;font-size:25px;font-weight:600}
.user{position:absolute;left:766px;top:21px;display:flex;align-items:center}
.bell{position:relative;width:20px;height:20px;margin-right:18px}
.bell .badge{position:absolute;right:-6px;top:-8px;width:14px;height:14px;border-radius:50%;background:#8a7a2c;color:#fff;font-size:8.5px;display:flex;align-items:center;justify-content:center}
.avatar-user{width:29px;height:29px;border-radius:50%;background:linear-gradient(#5a5f66,#2c3036);margin-right:9px}
.user-name{font-size:13px;font-weight:600;line-height:16px}
.user-role{font-size:10px;color:var(--muted)}
.caret{margin-left:16px;width:0;height:0;border-left:5px solid transparent;border-right:5px solid transparent;border-top:5px solid var(--muted)}
.card{position:absolute;left:26px;width:908px;background:var(--card);border-radius:10px}
.card-head{height:76px;display:flex;align-items:center;padding:0 20px;position:relative}
.card-title{font-size:16.5px;font-weight:600}
.card-sub{font-size:14px;font-weight:500;color:var(--link);margin-left:9px}
.partner{position:absolute;left:490px;width:200px;text-align:center;font-size:12px;font-weight:600;color:#7a7f87}
.search{position:absolute;left:820px;width:34px;height:34px;border-radius:50%;background:#fff;display:flex;align-items:center;justify-content:center}
.btn-add{position:absolute;left:869px;width:164px;height:36px;border-radius:18px;background:var(--red);color:#fff;font-size:14px;font-weight:600;display:flex;align-items:center;justify-content:center;gap:8px}
.card .btn-add{left:auto;right:20px}
.card .search{left:auto;right:218px}
table{position:absolute;left:21px;top:77px;width:866px;border-collapse:collapse;background:#fff;border-radius:6px;overflow:hidden;font-size:12px}
thead tr{background:var(--head);color:#fff;height:44px}
th{text-align:left;font-weight:500;font-size:12.5px}
th .sort{opacity:.6;margin-left:6px;font-size:11px}
tbody tr{height:58px}
td{vertical-align:middle}
.person{display:flex;align-items:center;gap:7px;font-weight:500}
.person .pic{width:31px;height:31px;border-radius:50%;background:linear-gradient(#b7a89a,#5b5048)}
.actions{display:flex;gap:7px}
.act{width:32px;height:32px;border-radius:50%;background:var(--chip);display:flex;align-items:center;justify-content:center}
.act svg{width:12px;height:12px}
</style>
</head>
<body>
<aside class="sidebar">
  <div class="brand"><span class="mark"></span><span>MERIDIAN<br>WORKS</span></div>
  <div class="btn-report"><svg width="14" height="14" viewBox="0 0 14 14"><path d="M7 1v12M1 7h12" stroke="#fff" stroke-width="1.6"/></svg>New Report</div>
  <ul class="nav">
    <li class="active"><svg viewBox="0 0 16 16"><rect x="1" y="1" width="14" height="14" rx="3"/><path d="M1 6h14M7 6v9" stroke="#0b4a82" stroke-width="1.4"/></svg>Dashboard</li>
    <li><svg viewBox="0 0 16 16"><rect x="1" y="1" width="14" height="10" rx="2"/><rect x="6" y="12" width="4" height="3"/></svg>Applications</li>
    <li><svg viewBox="0 0 16 16"><rect x="1" y="1" width="14" height="14" rx="3"/><path d="M4 6h8M4 10h8" stroke="#0b4a82" stroke-width="1.4"/></svg>Transcript Request</li>
    <li><svg viewBox="0 0 16 16"><rect x="1" y="3" width="11" height="12" rx="2"/><circle cx="12" cy="12" r="3.5"/></svg>New Hire Packet</li>
    <li><svg viewBox="0 0 16 16"><circle cx="8" cy="8" r="7"/><circle cx="8" cy="8" r="2.5" fill="#1366a6"/></svg>Setting</li>
  </ul>
  <div class="logout"><svg width="16" height="16" viewBox="0 0 16 16" fill="none" stroke="#fff" stroke-width="1.5"><path d="M6 2H2v12h4M7 8h8M12 5l3 3-3 3"/></svg>Log Out</div>
  <div class="copy">© 2025 Meridian Works.<br>All rights reserved.</div>
</aside>

<main class="main">
  <h1 class="title">Dashboard</h1>
  <div class="user">
    <div class="bell"><svg width="16" height="20" viewBox="0 0 16 20"><path d="M8 2a5 5 0 0 0-5 5v5l-2 3h14l-2-3V7a5 5 0 0 0-5-5zM6 17a2 2 0 0 0 4 0z" fill="#9aa0a8"/></svg><span class="badge">8</span></div>
    <div class="avatar-user" role="img" aria-label="User profile photo"></div>
    <div><div class="user-name">Dana R</div><div class="user-role">Account Role</div></div>
    <div class="caret"></div>
  </div>

  <section class="card" style="top:80px;height:433px">
    <div class="card-head">
      <span class="card-title">Ledger Book Demo Test:</span><span class="card-sub">Students</span>
      <span class="partner">Meridian Works</span>
      <span class="search"><svg width="14" height="14" viewBox="0 0 14 14" fill="none" stroke="#16181d" stroke-width="1.5"><circle cx="6" cy="6" r="4.5"/><path d="M9.5 9.5L13 13"/></svg></span>
      <span class="btn-add"><svg width="13" height="13" viewBox="0 0 14 14"><path d="M7 1v12M1 7h12" stroke="#fff" stroke-width="1.6"/></svg>Add Student</span>
    </div>
    <table>
      <thead><tr>
        <th style="width:43px;padding-left:16px">#</th>
        <th style="width:219px">Employee Name<span class="sort">⇅</span></th>
        <th style="width:131px">Grade<span class="sort">⇅</span></th>
        <th style="width:131px">Year<span class="sort">⇅</span></th>
        <th style="width:219px">School Building<span class="sort">⇅</span></th>
        <th>Actions<span class="sort">⇅</span></th>
      </tr></thead>
      <tbody>
        <tr><td style="padding-left:16px">1</td><td><div class="person"><span class="pic" role="img" aria-label="Student photo"></span>Owen Hale</div></td><td>11</td><td>2000</td><td>Northfield High School</td><td><div class="actions"><span class="act"><svg viewBox="0 0 12 12"><path d="M6 1v10M1 6h10" stroke="#222" stroke-width="1.3"/></svg></span><span class="act"><svg viewBox="0 0 12 12"><path d="M2 10l1-3 5-5 2 2-5 5zM1 11.5h10" stroke="#222" stroke-width="1.3" fill="#222"/></svg></span><span class="act"><svg viewBox="0 0 12 12" fill="none" stroke="#222" stroke-width="1.2"><path d="M1.5 3h9M4.5 3V1.5h3V3M2.5 3l.7 8h5.6l.7-8M5 5v4M7 5v4"/></svg></span></div></td></tr>
        <tr><td style="padding-left:16px">2</td><td><div class="person"><span class="pic" role="img" aria-label="Student photo"></span>Eli Marsh</div></td><td>01</td><td>2014</td><td>Linden School</td><td><div class="actions"><span class="act"><svg viewBox="0 0 12 12"><path d="M6 1v10M1 6h10" stroke="#222" stroke-width="1.3"/></svg></span><span class="act"><svg viewBox="0 0 12 12"><path d="M2 10l1-3 5-5 2 2-5 5zM1 11.5h10" stroke="#222" stroke-width="1.3" fill="#222"/></svg></span><span class="act"><svg viewBox="0 0 12 12" fill="none" stroke="#222" stroke-width="1.2"><path d="M1.5 3h9M4.5 3V1.5h3V3M2.5 3l.7 8h5.6l.7-8M5 5v4M7 5v4"/></svg></span></div></td></tr>
        <tr><td style="padding-left:16px">3</td><td><div class="person"><span class="pic" role="img" aria-label="Student photo"></span>Tomas</div></td><td>03</td><td>2018</td><td>Harbor School</td><td><div class="actions"><span class="act"><svg viewBox="0 0 12 12"><path d="M6 1v10M1 6h10" stroke="#222" stroke-width="1.3"/></svg></span><span class="act"><svg viewBox="0 0 12 12"><path d="M2 10l1-3 5-5 2 2-5 5zM1 11.5h10" stroke="#222" stroke-width="1.3" fill="#222"/></svg></span><span class="act"><svg viewBox="0 0 12 12" fill="none" stroke="#222" stroke-width="1.2"><path d="M1.5 3h9M4.5 3V1.5h3V3M2.5 3l.7 8h5.6l.7-8M5 5v4M7 5v4"/></svg></span></div></td></tr>
        <tr><td style="padding-left:16px">4</td><td><div class="person"><span class="pic" role="img" aria-label="Student photo"></span>Noah Brandt</div></td><td>08</td><td>2020</td><td>Maple Academy</td><td><div class="actions"><span class="act"><svg viewBox="0 0 12 12"><path d="M6 1v10M1 6h10" stroke="#222" stroke-width="1.3"/></svg></span><span class="act"><svg viewBox="0 0 12 12"><path d="M2 10l1-3 5-5 2 2-5 5zM1 11.5h10" stroke="#222" stroke-width="1.3" fill="#222"/></svg></span><span class="act"><svg viewBox="0 0 12 12" fill="none" stroke="#222" stroke-width="1.2"><path d="M1.5 3h9M4.5 3V1.5h3V3M2.5 3l.7 8h5.6l.7-8M5 5v4M7 5v4"/></svg></span></div></td></tr>
        <tr><td style="padding-left:16px">5</td><td><div class="person"><span class="pic" role="img" aria-label="Student photo"></span>Felix Orr</div></td><td>05</td><td>2024</td><td>Crestview Global School</td><td><div class="actions"><span class="act"><svg viewBox="0 0 12 12"><path d="M6 1v10M1 6h10" stroke="#222" stroke-width="1.3"/></svg></span><span class="act"><svg viewBox="0 0 12 12"><path d="M2 10l1-3 5-5 2 2-5 5zM1 11.5h10" stroke="#222" stroke-width="1.3" fill="#222"/></svg></span><span class="act"><svg viewBox="0 0 12 12" fill="none" stroke="#222" stroke-width="1.2"><path d="M1.5 3h9M4.5 3V1.5h3V3M2.5 3l.7 8h5.6l.7-8M5 5v4M7 5v4"/></svg></span></div></td></tr>
      </tbody>
    </table>
  </section>

  <section class="card" style="top:533px;height:75px">
    <div class="card-head" style="height:75px">
      <span class="card-title">Ledger Book Demo Test:</span><span class="card-sub">Students</span>
      <span class="partner">Demo District</span>
      <span class="search"><svg width="14" height="14" viewBox="0 0 14 14" fill="none" stroke="#16181d" stroke-width="1.5"><circle cx="6" cy="6" r="4.5"/><path d="M9.5 9.5L13 13"/></svg></span>
      <span class="btn-add"><svg width="13" height="13" viewBox="0 0 14 14"><path d="M7 1v12M1 7h12" stroke="#fff" stroke-width="1.6"/></svg>Add Student</span>
    </div>
  </section>

  <section class="card" style="top:629px;height:74px">
    <div class="card-head" style="height:74px">
      <span class="card-title">Ledger Book Demo Test:</span><span class="card-sub">Students</span>
      <span class="partner">Eastvale Tech</span>
      <span class="search"><svg width="14" height="14" viewBox="0 0 14 14" fill="none" stroke="#16181d" stroke-width="1.5"><circle cx="6" cy="6" r="4.5"/><path d="M9.5 9.5L13 13"/></svg></span>
      <span class="btn-add"><svg width="13" height="13" viewBox="0 0 14 14"><path d="M7 1v12M1 7h12" stroke="#fff" stroke-width="1.6"/></svg>Add Student</span>
    </div>
  </section>
</main>
</body>
</html>
```